Loftvane.ca Your Canadian Source for all your mortgage needs.

I need to get a fresh look on my current website. It is not currently a Wordpress site and i need to build a whole new site that i can do my editing in using Wordpress.
I need it built in a mobile or responsive theme.
There will be a secured application page which is critical.
I have 3 books written so i want to be able to have advertising spaces for promoting them and a landing page ( I can build my own landing pages)
I need the frame work of a professional theme with easy editing capabilities.
I have my own LOGOs which i would continue to use. The current site can be reviewed at www.loftvane.ca.
The front page could have a young couple near a nice house, open to suggestions.
I don't need a blog post to update but if it was on the sides of the pages I could use it. Something like a "Latest News" section.
I would like to have a Main page, Application Page, Resource page, Contact page, Calculator Page, a questions and answer page. Theses can be populated with the current information or I can add latter.
I want the main page to be a mini sales page so I can link to Posts on First Time Home Buyers, Refinance Options, Second Home or New purchase options.
I provide mortgages for people across Canada so i want the Canadian Flag incorporated
I like the colors to work with the logo colors on the current site

Target Market(s)

Canadian Mortgage Clients

Font styles to use
Sans Serif

Colors
3277b5
cadf82

Requirements
Must have
• Must work in a Wordpress Theme
• Please see Project description for more details
Nice to have
• Space to add banner ads for my books. I have 3 books written

```html
<!DOCTYPE html>
<html lang="en">
<head>
<meta charset="utf-8">
<title>Loftvane.ca – Your Canadian Source for Mortgages</title>
<link rel="stylesheet" href="https://fonts.googleapis.com/css2?family=Open+Sans:wght@400;600;700;800&display=swap">
<style>
:root{
  --blue:#3277b5;
  --blue-dark:#1f5a94;
  --navy:#17406b;
  --green:#cadf82;
  --green-dark:#8fb13a;
  --text:#4a4a4a;
  --muted:#8a8f96;
  --page:#e9eef3;
  --white:#fff;
  --red:#d52b1e;
}
*{box-sizing:border-box;margin:0;padding:0}
html,body{width:1200px;height:2384px;overflow:hidden}
body{font-family:"Open Sans",Arial,sans-serif;color:var(--text);background:var(--page)}
.site{width:1200px;height:2384px;position:relative;background:var(--white)}

/* header */
.header{height:108px;display:flex;align-items:center;justify-content:space-between;padding:0 40px;background:var(--white)}
.brand{display:flex;align-items:center;gap:12px;font-weight:800;font-size:46px;color:var(--blue);letter-spacing:1px}
.brand-mark{width:30px;height:30px;background:var(--green)}
.header-right{display:flex;align-items:center;gap:24px}
.flags{display:flex;gap:10px}
.call{display:flex;align-items:center;gap:10px}
.call-icon{width:40px;height:40px;border-radius:50%;background:var(--blue);display:flex;align-items:center;justify-content:center}
.call small{display:block;font-size:13px;color:var(--muted);font-weight:700}
.call strong{font-size:22px;color:var(--navy);font-weight:800}

/* nav */
.nav{height:44px;background:var(--blue);display:flex;align-items:center;justify-content:space-between;padding:0 40px}
.nav ul{list-style:none;display:flex;gap:0}
.nav li{color:var(--white);font-weight:700;font-size:15px;padding:0 24px;line-height:44px}
.nav li.active{background:var(--blue-dark)}
.social{display:flex;gap:8px}
.social span{width:26px;height:26px;border-radius:50%;background:var(--white)}

/* hero */
.hero{position:relative;height:568px;background:linear-gradient(180deg,#7fb2de 0%,#a9cdea 40%,#8fae6c 78%,#5f8740 100%)}
.hero-copy{position:absolute;left:620px;top:90px;width:520px;color:var(--white);text-shadow:0 2px 6px rgba(0,0,0,.35)}
.hero-copy h1{font-size:44px;font-weight:800;line-height:1.1}
.hero-copy p{font-size:20px;font-weight:700;text-transform:uppercase;line-height:1.35;margin-top:8px}
.hero-arrow{position:absolute;top:250px;width:26px;height:48px;background:rgba(0,0,0,.45);display:flex;align-items:center;justify-content:center}
.hero-arrow.left{left:0}.hero-arrow.right{right:0}

/* features */
.features{position:absolute;top:658px;left:70px;width:1060px;display:flex;justify-content:space-between}
.feature{width:320px;text-align:center}
.feature-icon{width:110px;height:110px;margin:0 auto -34px;border-radius:50%;background:var(--blue);border:6px solid var(--white);position:relative;z-index:2;display:flex;align-items:center;justify-content:center}
.feature-box{background:#f4f8ec;border:3px solid var(--green);padding:42px 20px 18px;height:178px}
.feature-box h3{font-size:20px;font-weight:800;color:var(--blue);line-height:1.1}
.feature-box h4{font-size:12px;font-weight:700;color:var(--navy);text-transform:uppercase;margin-top:2px}
.feature-box p{font-size:12px;line-height:1.4;margin-top:6px}
.btn-small{display:inline-block;margin-top:10px;background:var(--blue);color:var(--white);font-size:12px;font-weight:700;padding:5px 14px;border-radius:3px}

/* broker */
.broker{position:absolute;top:920px;left:40px;width:1120px;display:flex;gap:50px}
.broker-text{width:820px}
.broker-text h2{font-size:30px;font-weight:800;color:var(--blue);margin-bottom:18px}
.broker-text p{font-size:16px;line-height:1.55;margin-bottom:20px}
.books{display:flex;flex-direction:column;gap:28px;padding-top:10px}
.book{width:240px;height:220px;background:linear-gradient(135deg,#f2c94c,#d76a2b 55%,#7a9a3a);border:6px solid #d9c6a2}

/* newsletter */
.newsletter{position:absolute;top:1760px;left:0;width:1200px;height:210px;background:#f3f6f9;border-top:1px solid #dbe3ea;border-bottom:1px solid #dbe3ea;text-align:center;padding-top:30px}
.newsletter h2{font-size:30px;font-weight:700;color:var(--blue)}
.newsletter .rule{width:420px;height:2px;background:var(--green);margin:10px auto 14px}
.newsletter p{font-size:16px;font-weight:700;color:var(--navy)}
.subscribe{display:flex;justify-content:center;margin-top:16px}
.subscribe .field{width:600px;height:48px;border:1px solid #cdd6df;background:var(--white);text-align:left;padding:0 16px;line-height:46px;font-size:14px;color:var(--muted)}
.subscribe .go{width:170px;height:48px;background:var(--blue);color:var(--white);font-weight:700;font-size:14px;line-height:48px}

/* footer */
.footer{position:absolute;top:2032px;left:0;width:1200px;height:352px;background:var(--navy);color:#c8d6e6}
.questions{height:84px;background:var(--blue);display:flex;align-items:center;padding:0 40px;gap:60px}
.questions h3{color:var(--green);font-size:26px;font-weight:800;line-height:1}
.q-item{display:flex;align-items:center;gap:10px;color:var(--white);font-weight:700;font-size:13px;text-transform:uppercase;line-height:1.2}
.q-icon{width:36px;height:36px;border-radius:50%;border:2px solid var(--white);display:flex;align-items:center;justify-content:center}
.footer-cols{display:flex;padding:22px 40px;gap:40px;height:220px}
.footer-cols h4{color:var(--white);font-size:16px;font-weight:700;margin-bottom:10px}
.footer-cols p,.footer-cols li{font-size:13px;line-height:1.6}
.col{width:250px}
.col ul{list-style:none}
.news-date{color:var(--green);font-size:12px}
.footer .social span{width:32px;height:32px;background:var(--blue)}
.copyright{position:absolute;bottom:0;width:100%;height:46px;background:#0f2e50;text-align:center;line-height:46px;font-size:13px}
</style>
</head>
<body>
<div class="site">
  <header class="header">
    <div class="brand"><span class="brand-mark"></span>Loftvane</div>
    <div class="header-right">
      <div class="flags">
        <svg width="48" height="28" viewBox="0 0 48 28" role="img" aria-label="Canadian flag"><rect width="12" height="28" fill="#d52b1e"/><rect x="12" width="24" height="28" fill="#fff" stroke="#ddd"/><rect x="36" width="12" height="28" fill="#d52b1e"/><path d="M24 6l4 8-4 8-4-8z" fill="#d52b1e"/></svg>
        <svg width="48" height="28" viewBox="0 0 48 28" role="img" aria-label="Canadian flag"><rect width="12" height="28" fill="#d52b1e"/><rect x="12" width="24" height="28" fill="#fff" stroke="#ddd"/><rect x="36" width="12" height="28" fill="#d52b1e"/><path d="M24 6l4 8-4 8-4-8z" fill="#d52b1e"/></svg>
      </div>
      <div class="call">
        <div class="call-icon"><svg width="20" height="20" viewBox="0 0 24 24"><path d="M6.6 10.8a15 15 0 006.6 6.6l2.2-2.2c.3-.3.7-.4 1-.2 1.1.4 2.3.6 3.6.6.6 0 1 .4 1 1V20c0 .6-.4 1-1 1A17 17 0 013 4c0-.6.4-1 1-1h3.5c.6 0 1 .4 1 1 0 1.3.2 2.5.6 3.6.1.3 0 .7-.2 1z" fill="#fff"/></svg></div>
        <div><small>CALL US</small><strong>403-555-0148</strong></div>
      </div>
    </div>
  </header>

  <nav class="nav">
    <ul><li class="active">HOME</li><li>APPLICATION</li><li>RESOURCE</li><li>CALCULATOR</li><li>FAQS</li><li>CONTACT US</li></ul>
    <div class="social"><span></span><span></span><span></span></div>
  </nav>

  <section class="hero" role="img" aria-label="Young couple smiling in front of a house with a garden lawn">
    <div class="hero-copy">
      <h1>CUSTOMIZE YOUR MORTGAGE</h1>
      <p>and look how to save thousands of dollars on our current mortgage</p>
    </div>
    <div class="hero-arrow left"><svg width="12" height="20" viewBox="0 0 12 20"><path d="M10 2L2 10l8 8" stroke="#fff" stroke-width="3" fill="none"/></svg></div>
    <div class="hero-arrow right"><svg width="12" height="20" viewBox="0 0 12 20"><path d="M2 2l8 8-8 8" stroke="#fff" stroke-width="3" fill="none"/></svg></div>
  </section>

  <div class="features">
    <div class="feature">
      <div class="feature-icon"><svg width="48" height="48" viewBox="0 0 48 48"><rect x="10" y="6" width="28" height="36" rx="2" fill="none" stroke="#fff" stroke-width="3"/><path d="M16 16h16M16 23h16M16 30h10" stroke="#fff" stroke-width="3"/></svg></div>
      <div class="feature-box"><h3>APPLY ONLINE NOW!</h3><p>We lined up the banks and get your lowest rates and terms with NO FEES or costs to you.</p><span class="btn-small">Click Here »</span></div>
    </div>
    <div class="feature">
      <div class="feature-icon"><svg width="48" height="48" viewBox="0 0 48 48"><circle cx="24" cy="24" r="16" fill="none" stroke="#fff" stroke-width="3"/><path d="M24 14v20M29 18h-7a3 3 0 000 6h4a3 3 0 010 6h-7" stroke="#fff" stroke-width="3" fill="none"/></svg></div>
      <div class="feature-box"><h3>SAVE THOUSANDS</h3><h4>On your mortgage</h4><p>Customize your own mortgage to fit your financial needs.</p><span class="btn-small">View VIDEO Document »</span></div>
    </div>
    <div class="feature">
      <div class="feature-icon"><svg width="48" height="48" viewBox="0 0 48 48"><rect x="12" y="6" width="24" height="36" rx="2" fill="none" stroke="#fff" stroke-width="3"/><rect x="16" y="10" width="16" height="7" fill="#fff"/><path d="M17 23h3M23 23h3M29 23h2M17 29h3M23 29h3M29 29h2M17 35h3M23 35h3M29 35h2" stroke="#fff" stroke-width="3"/></svg></div>
      <div class="feature-box"><h3>MORTGAGE CALCULATORS</h3><p>Work out payments, savings and terms in a few quick steps.</p><span class="btn-small">Click Here »</span></div>
    </div>
  </div>

  <section class="broker">
    <div class="broker-text">
      <h2>WHY USE A MORTGAGE BROKER?</h2>
      <p>Professional representation for you and your family to help negotiate one of your biggest investments in your life. Helping you plan your mortgage to save you the most money.</p>
      <p>A personalized "Mortgage Action Plan" which helps you to plan your mortgage that best suits you and your families needs. Teaching you how to save thousands on your mortgage and allowing you to review and compare options both today and into the future.</p>
      <p>Personal Service at your convenience "Where you want it when you want it".</p>
      <p>We will help you save Thousands with rate discounts and other mortgage tips. At the same time keeping you informed of new products or developments that would benefit you and your family.</p>
      <p>More choices for rates and terms from across the country. We negotiate for you and can deal with multiple lenders in the same time it takes you to deal with one.</p>
      <p>We can teach you how to rebuild your credit so that your dream of home ownership can become a reality sooner.</p>
      <p>NO FEES or costs to you (in most cases). We beat up the banks and lenders to get you the best rates and terms then the lenders have to pay us. Which simply means there is no cost to you and your family (O.A.C).</p>
      <p>We help all types of clients from AAA to as Bankrupt. We have case down to No down payment mortgages. We offer complete consultation to which type of mortgage will benefit you the most.</p>
      <p>24/7 Access.</p>
    </div>
    <div class="books">
      <div class="book" role="img" aria-label="Cover of the book on first time home buyers"></div>
      <div class="book" role="img" aria-label="Cover of the second mortgage book"></div>
      <div class="book" role="img" aria-label="Cover of the book on saving thousands on your mortgage"></div>
    </div>
  </section>

  <section class="newsletter">
    <h2>Get Our Newsletters</h2>
    <div class="rule"></div>
    <p>Want To Be On Our Mailing List? Get Our Newsletter.</p>
    <div class="subscribe"><div class="field">Enter your email address</div><div class="go">SUBSCRIBE NOW</div></div>
  </section>

  <footer class="footer">
    <div class="questions">
      <h3>HAVE<br>QUESTIONS?</h3>
      <div class="q-item"><span class="q-icon"><svg width="16" height="16" viewBox="0 0 24 24"><path d="M6.6 10.8a15 15 0 006.6 6.6l2.2-2.2c.3-.3.7-.4 1-.2 1.1.4 2.3.6 3.6.6.6 0 1 .4 1 1V20c0 .6-.4 1-1 1A17 17 0 013 4c0-.6.4-1 1-1h3.5c.6 0 1 .4 1 1 0 1.3.2 2.5.6 3.6.1.3 0 .7-.2 1z" fill="#fff"/></svg></span>Call us<br>403-555-0148</div>
      <div class="q-item"><span class="q-icon"><svg width="18" height="14" viewBox="0 0 18 14"><rect x="1" y="1" width="16" height="12" fill="none" stroke="#fff" stroke-width="2"/><path d="M1 1l8 7 8-7" stroke="#fff" stroke-width="2" fill="none"/></svg></span>Send us<br>an email</div>
      <div class="q-item"><span class="q-icon"><svg width="14" height="18" viewBox="0 0 14 18"><path d="M7 1a6 6 0 016 6c0 4-6 10-6 10S1 11 1 7a6 6 0 016-6z" fill="#fff"/><circle cx="7" cy="7" r="2" fill="#3277b5"/></svg></span>Find a<br>local office</div>
      <div class="q-item"><span class="q-icon"><svg width="14" height="18" viewBox="0 0 14 18"><text x="7" y="15" text-anchor="middle" font-size="16" font-weight="700" fill="#fff" font-family="Open Sans, sans-serif">?</text></svg></span>Read the<br>FAQs</div>
    </div>
    <div class="footer-cols">
      <div class="col"><h4>Contact Us</h4><p>Loftvane Mortgages Inc.<br>210, 4480 Birchfield Way NW<br>Calgary, Alberta T3A 0B9</p></div>
      <div class="col"><h4>Latest News</h4>
        <p class="news-date">January 28, 2015 • 11:44am</p><p>New first time buyer incentives announced this week.</p>
        <p class="news-date">January 26, 2015 • 9:20am</p><p>Fixed rates hold steady across most major lenders.</p>
      </div>
      <div class="col"><h4>Quick links</h4><ul><li>Home</li><li>Application</li><li>Resource</li><li>Calculator</li><li>FAQ's</li><li>Contact Us</li></ul></div>
      <div class="col"><h4>Connect with us</h4><div class="social"><span></span><span></span><span></span></div></div>
    </div>
    <div class="copyright">© 2015 Loftvane Mortgages. All Rights Reserved. • Terms and Conditions • Privacy Policy • Terms of Use</div>
  </footer>
</div>
</body>
</html>
```